M25 Billboard Advert Required Please

I need an advert for a motorway Billboard on the M25 , the advert should show the following in big letters:
GUTTER CLEANING
DALRYNFLUES.COM and a small logo off to the side (Our logo is attached)

The printer has requested the following (Important please) the advert has to be
pdf file / 300 dpi/landscape orientation / scaled to a minimum 25% advert size ( this particular site is 22ft x 10ft so 25% of this please). Please also make sure that the artwork is embedded and outlined correctly if this is incorrect it will affect the printing of the banner.

Target Market(s)

General Public

Industry/Entity Type

Gutter Cleaning

Requirements
Should not have
• No Change to our Logo

```html
<!DOCTYPE html>
<html lang="en">
<head>
<meta charset="utf-8">
<title>Gutter Cleaning – Billboard</title>
<link href="https://fonts.googleapis.com/css2?family=Montserrat:ital,wght@0,600;0,700;1,800;1,900&display=swap" rel="stylesheet">
<style>
  :root {
    --page-bg: #9c9c9c;
    --board-black: #050505;
    --board-charcoal: #1c1c1c;
    --band-white: #ffffff;
    --ink: #1a1a1a;
    --accent-red: #d3212c;
    --silver-top: #ffffff;
    --silver-mid: #d9d9db;
    --silver-low: #8c8c90;
  }
  * { margin: 0; padding: 0; box-sizing: border-box; }
  html, body {
    width: 887px;
    height: 1200px;
    overflow: hidden;
    background: var(--page-bg);
    font-family: "Montserrat", Arial, sans-serif;
  }
  .canvas {
    position: relative;
    width: 887px;
    height: 1200px;
  }
  .billboard {
    position: absolute;
    left: 37px;
    top: 416px;
    width: 813px;
    height: 368px;
    box-shadow: 0 6px 14px rgba(0, 0, 0, 0.35);
    overflow: hidden;
  }
  .headline-panel {
    position: absolute;
    left: 0;
    top: 0;
    width: 100%;
    height: 266px;
    background:
      radial-gradient(ellipse at 70% 20%, var(--board-charcoal) 0%, transparent 55%),
      radial-gradient(ellipse at 20% 80%, #141414 0%, transparent 50%),
      var(--board-black);
  }
  .headline-panel svg { display: block; }
  .headline-text {
    font-family: "Montserrat", Arial, sans-serif;
    font-style: italic;
    font-weight: 800;
    font-size: 128px;
    letter-spacing: 3px;
    fill: url(#silver);
    stroke: var(--silver-top);
    stroke-width: 3;
    stroke-linejoin: round;
    paint-order: stroke fill;
  }
  .silver-top { stop-color: var(--silver-top); }
  .silver-mid { stop-color: var(--silver-mid); }
  .silver-low { stop-color: var(--silver-low); }
  .info-band {
    position: absolute;
    left: 0;
    top: 266px;
    width: 100%;
    height: 102px;
    background: var(--band-white);
  }
  .web-address {
    position: absolute;
    left: 24px;
    top: 32px;
    font-style: italic;
    font-weight: 800;
    font-size: 29px;
    letter-spacing: 1.2px;
    color: var(--ink);
    text-shadow: 1px 2px 3px rgba(0, 0, 0, 0.25);
    white-space: nowrap;
  }
  .divider {
    position: absolute;
    left: 538px;
    top: 14px;
    width: 6px;
    height: 64px;
    background: var(--accent-red);
    transform: skewX(-8deg);
  }
  .brand {
    position: absolute;
    left: 572px;
    top: 20px;
    width: 220px;
  }
  .brand-name {
    font-weight: 700;
    font-size: 30px;
    color: var(--ink);
    line-height: 1;
    white-space: nowrap;
    text-align: right;
  }
  .brand-tagline {
    margin-top: 10px;
    font-weight: 600;
    font-size: 11px;
    color: var(--ink);
    white-space: nowrap;
    text-align: right;
  }
</style>
</head>
<body>
<main class="canvas">
  <section class="billboard">
    <div class="headline-panel">
      <svg width="813" height="266" viewBox="0 0 813 266">
        <defs>
          <linearGradient id="silver" x1="0" y1="0" x2="0" y2="1">
            <stop offset="0" class="silver-top"/>
            <stop offset="0.45" class="silver-mid"/>
            <stop offset="1" class="silver-low"/>
          </linearGradient>
          <filter id="drop" x="-5%" y="-5%" width="110%" height="120%">
            <feDropShadow dx="2" dy="4" stdDeviation="3" flood-color="#000" flood-opacity="0.7"/>
          </filter>
        </defs>
        <text class="headline-text" x="30" y="121" filter="url(#drop)">GUTTER</text>
        <text class="headline-text" x="30" y="243" filter="url(#drop)">CLEANING</text>
      </svg>
    </div>
    <div class="info-band">
      <p class="web-address">WWW.DALRYNFLUES.COM</p>
      <span class="divider" aria-hidden="true"></span>
      <div class="brand">
        <p class="brand-name">Dalryn Flues</p>
        <p class="brand-tagline">Clean gutters protect your property</p>
      </div>
    </div>
  </section>
</main>
</body>
</html>
```